Website design for an award-winning animation studio

We are an animation studio launching our new corporate website. We need a web designer/developer to produce a professional business website for us. We have competitors' websites and a early web demo/web layout for reference. We cater to the global audience.

Attached is the brief to website designer. There are 4 points of brief details for the designer. Please read through. We will provide the images only after award.

Target Market(s)

Our website caters to potential B2B clients, investors, fellow media & animation industry players, future employees, parents, kids, whoever wants to know us better.

Industry/Entity Type

Business

Number of Pages Required

5+ page

Requirements
Must have
• Brief 1: Reference sites
• For the key reference site: https://wow.plumvale.example/insider/2016/04/22/quiet-gears-debut/. The color and font gives a very current day feel.
• Other references:
• Demo site: http://talver-works.example/temp/web_beta.html
• Current site: http://talver-works.example/
• Some more References sites:
• http://www.brindlequay.example/
• https://thecorvanhollisgroup.example/
• http://www.foxglenmotion.example/
• Brief 2: Template
• Template to use:
• http://themes.kitlayout.example/prism-v1.2.0/sample-04-half-image-slider.html
• Brief 3: Images
• Images to use: We will pass you the images once upon award
• Brief 4: Cater to content
• I attached the word doc. This is a brief for the website designer to get a sense of what content the website will cater to.
• Our website caters to potential B2B clients, investors, fellow industry players, future employees, parents, kids, whoever wants to know us better.
• Our content write up will be professional yet fun, positive and engaging.

```html
<!DOCTYPE html>
<html lang="en">
<head>
<meta charset="utf-8">
<title>Talver Works — Animation Studio</title>
<link rel="stylesheet" href="https://fonts.googleapis.com/css2?family=Open+Sans:wght@400;600;700;800&display=swap">
<style>
:root{
  --crimson:#d8234b;
  --crimson-dark:#a81636;
  --yellow:#f2c21b;
  --teal:#1fd3c6;
  --charcoal:#2b2b2b;
  --ink:#333;
  --muted:#777;
  --white:#fff;
  --paper:#f6f6f6;
}
*{box-sizing:border-box;margin:0;padding:0}
html,body{width:1200px;height:5248px;overflow:hidden}
body{position:relative;font-family:"Open Sans",Arial,sans-serif;color:var(--ink);background:var(--white)}
.section-title{position:absolute;left:0;width:1200px;text-align:center;font-size:40px;font-weight:600}
.section-title::after{content:"";display:block;width:70px;height:4px;background:var(--crimson);margin:16px auto 0}
.on-dark{color:var(--white)}
.on-dark::after{background:var(--white)}

/* header */
.site-header{position:absolute;left:0;top:0;width:1200px;height:165px;z-index:3}
.header-bar{position:absolute;left:0;top:0;width:1200px;height:115px;background:var(--crimson-dark)}
.brand{position:absolute;left:100px;top:36px;display:flex;align-items:center;gap:14px;color:var(--white);font-size:30px;font-weight:800;letter-spacing:3px}
.brand-dot{width:38px;height:38px;border-radius:50%;background:var(--white)}
.social{position:absolute;right:95px;top:40px;display:flex;gap:10px}
.social span{width:34px;height:34px;border:2px solid var(--white);background:var(--crimson)}
.main-nav{position:absolute;left:0;top:115px;width:1200px;height:50px;background:var(--crimson);display:flex;justify-content:flex-end;align-items:center;gap:30px;padding-right:95px}
.main-nav a{color:var(--white);font-size:13px;font-weight:600;text-decoration:none;letter-spacing:.5px}

/* hero */
.hero{position:absolute;left:0;top:0;width:1200px;height:740px;background:linear-gradient(180deg,#9fd1f0 0%,#c8e6f7 45%,#f0d3c8 80%,#e7b9a7 100%);clip-path:polygon(0 0,100% 0,100% 100%,0 94%)}
.hero-tagline{position:absolute;left:300px;top:500px;font-size:38px;font-weight:800;line-height:1.42;color:var(--white)}
.hero-tagline span{background:var(--crimson);padding:2px 12px;box-decoration-break:clone;-webkit-box-decoration-break:clone}

/* story */
.story-text{position:absolute;left:250px;top:870px;width:700px;text-align:center;font-size:13px;line-height:1.75;color:var(--muted)}

/* work */
.work{position:absolute;left:0;top:990px;width:1200px;height:780px;background:var(--yellow);clip-path:polygon(0 7%,100% 0,100% 94%,0 100%)}
.filters{position:absolute;left:0;top:1160px;width:1200px;display:flex;justify-content:center;gap:12px}
.filters span{background:var(--crimson);color:var(--white);font-size:13px;font-weight:700;padding:6px 14px}
.thumb{position:absolute;width:308px;height:165px}
.thumb-label{position:absolute;width:308px;text-align:center;font-size:16px;font-weight:600;color:var(--ink)}

/* services */
.service-tag{position:absolute;background:var(--crimson);color:var(--white);font-size:14px;font-weight:600;padding:4px 12px;transform:translateX(-50%)}
.service-line{position:absolute;width:0;border-left:2px dashed var(--crimson)}
.service-mark{position:absolute;width:120px;height:120px;border-radius:50%;background:var(--crimson);transform:translateX(-50%)}
.service-text{position:absolute;width:200px;text-align:center;font-size:11.5px;line-height:1.6;color:var(--muted);transform:translateX(-50%)}

/* partners */
.partners{position:absolute;left:0;top:2640px;width:1200px;height:610px;background:var(--charcoal);clip-path:polygon(0 8%,100% 0,100% 92%,0 100%)}
.partner-row{position:absolute;left:70px;top:2950px;width:1060px;display:flex;justify-content:space-between;align-items:center}
.partner{color:var(--white);font-size:24px;font-weight:800;letter-spacing:1px}
.dots{position:absolute;left:0;width:1200px;display:flex;justify-content:center;gap:8px}
.dots span{width:9px;height:9px;border-radius:50%;background:var(--white)}
.dots.grey span{background:#ccc}

/* news */
.news{position:absolute;width:300px}
.news h3{font-size:14px;font-weight:700;color:var(--ink);line-height:1.35;height:40px}
.news .meta{font-size:10.5px;color:#999;margin:10px 0 8px;display:flex;align-items:center;gap:8px}
.news .meta i{width:16px;height:12px;background:#bbb;display:inline-block}
.news p{font-size:11px;line-height:1.6;color:var(--muted)}
.news .more{display:block;margin-top:10px;font-size:10.5px;font-weight:700;color:var(--crimson)}

/* careers */
.careers{position:absolute;left:0;top:3830px;width:1200px;height:690px;background:var(--teal);clip-path:polygon(0 0,100% 8%,100% 92%,0 100%)}
.careers-intro{position:absolute;left:130px;top:4005px;width:940px;font-size:12px;line-height:1.6;color:var(--white)}
.careers-intro strong{display:block;margin-top:12px;font-weight:700}
.job{position:absolute;top:4140px;width:284px;height:315px;background:var(--white);box-shadow:0 4px 10px rgba(0,0,0,.15)}
.job-brand{height:120px;background:var(--paper);display:flex;align-items:center;justify-content:center;gap:10px;font-size:22px;font-weight:800;letter-spacing:2px;color:var(--ink)}
.job-brand i{width:28px;height:28px;border-radius:50%;background:var(--ink)}
.job-body{padding:16px 18px}
.job h4{font-size:15px;font-weight:700}
.job .tags{font-size:10px;color:#999;margin:8px 0;display:flex;gap:8px;align-items:center}
.job .tags b{background:var(--yellow);color:var(--ink);padding:1px 5px;font-weight:600}
.job .tags b.green{background:#5cb85c;color:var(--white)}
.job p{font-size:11px;line-height:1.55;color:var(--muted)}
.job-foot{position:absolute;left:18px;right:18px;bottom:18px;display:flex;justify-content:space-between;align-items:center}
.job-foot .pay{font-size:22px;font-weight:700;color:var(--crimson)}
.job-foot .pay small{font-size:10px;color:#999;font-weight:400}
.job-foot .apply{background:var(--crimson);color:var(--white);font-size:11px;font-weight:700;padding:6px 12px}

/* contact */
.contact{position:absolute;left:0;top:4490px;width:1200px;height:700px;background:var(--crimson);clip-path:polygon(0 4%,100% 0,100% 100%,0 100%)}
.contact-card{position:absolute;left:133px;top:4742px;width:935px;height:298px;background:var(--white)}
.contact-card .lead{position:absolute;left:40px;top:32px;width:420px;font-size:12px;line-height:1.6;color:var(--muted)}
.loc-title{position:absolute;left:40px;top:100px;background:var(--crimson);color:var(--white);font-size:13px;font-weight:700;padding:5px 12px}
.office{position:absolute;top:145px;width:200px;font-size:11px;line-height:1.55;color:var(--muted)}
.office b{display:block;color:var(--crimson);font-weight:700}
.map{position:absolute;left:515px;top:30px;width:390px;height:240px;background:linear-gradient(135deg,#eceae4,#dcd9d0)}

/* footer */
.site-footer{position:absolute;left:0;top:5162px;width:1200px;height:86px;background:var(--charcoal)}
.site-footer p{position:absolute;left:110px;top:34px;color:var(--white);font-size:12px;font-weight:600}
.to-top{position:absolute;left:1040px;top:18px;width:34px;height:34px;border-radius:50%;border:2px solid var(--crimson)}
</style>
</head>
<body>

<div class="hero" role="img" aria-label="Illustrated classroom scene with the studio's animated characters around a table"></div>

<header class="site-header">
  <div class="header-bar">
    <div class="brand"><span class="brand-dot"></span>TALVER WORKS</div>
    <div class="social" aria-label="Social links"><span></span><span></span><span></span><span></span><span></span></div>
  </div>
  <nav class="main-nav">
    <a>HOME</a><a>OUR STORY</a><a>OUR WORK</a><a>OUR SERVICES</a><a>OUR PARTNERS</a><a>NEWS</a><a>CAREER</a><a>CONTACT US</a>
  </nav>
</header>

<h1 class="hero-tagline"><span>We believe in the power of great<br>characters and wonderful<br>stories.</span></h1>

<h2 class="section-title" style="top:765px">Our Story</h2>
<p class="story-text">Talver Works is an award-winning animation and interactive studio based in Singapore, with offices in California, USA and Bangalore, India. We create original characters and stories for kids and grown-ups (who are really just grown-up kids), and we fuse the creative with the latest in interactive technology to bring our content to wherever our fans are.</p>

<section class="work"></section>
<h2 class="section-title on-dark" style="top:1045px">Our Work</h2>
<div class="filters"><span>TV</span><span>GAME</span><span>FILM</span><span>COMMERCIAL</span><span>AR/VR</span></div>

<div class="thumb" style="left:105px;top:1235px;background:linear-gradient(135deg,#6b6a5e,#c9b48a)" role="img" aria-label="Still from Mirage"></div>
<div class="thumb" style="left:445px;top:1235px;background:linear-gradient(135deg,#7fb4d6,#c89a5e)" role="img" aria-label="Still from Cap'n Whiffle"></div>
<div class="thumb" style="left:784px;top:1235px;background:linear-gradient(135deg,#8fc0de,#b98a54)" role="img" aria-label="Still from Gnomewick"></div>
<div class="thumb-label" style="left:105px;top:1413px">Mirage</div>
<div class="thumb-label" style="left:445px;top:1413px">Cap'n Whiffle</div>
<div class="thumb-label" style="left:784px;top:1413px">Gnomewick</div>

<div class="thumb" style="left:105px;top:1463px;background:linear-gradient(135deg,#2e2a3a,#6a5d7c)" role="img" aria-label="Still from Hana's Dream"></div>
<div class="thumb" style="left:445px;top:1463px;background:linear-gradient(135deg,#8ed0ee,#e8b95a)" role="img" aria-label="Still from Counting with Nora"></div>
<div class="thumb" style="left:784px;top:1463px;background:linear-gradient(135deg,#6dbb5c,#d9b24a)" role="img" aria-label="Still from Milo"></div>
<div class="thumb-label" style="left:105px;top:1641px">Hana's Dream</div>
<div class="thumb-label" style="left:445px;top:1641px">Counting with Nora</div>
<div class="thumb-label" style="left:784px;top:1641px">Milo</div>

<h2 class="section-title" style="top:1790px">Our Services</h2>

<div class="service-tag" style="left:217px;top:1910px">TV</div>
<div class="service-line" style="left:217px;top:1940px;height:50px"></div>
<div class="service-mark" style="left:217px;top:1990px" role="img" aria-label="Mascot holding a TV icon"></div>
<p class="service-text" style="left:217px;top:2130px">Talver Works creates original 3D animation content for TV that is both educational and entertaining.</p>

<div class="service-tag" style="left:465px;top:1910px">Commercials</div>
<div class="service-line" style="left:465px;top:1940px;height:100px"></div>
<div class="service-mark" style="left:465px;top:2040px" role="img" aria-label="Mascot holding a play icon"></div>
<p class="service-text" style="left:465px;top:2180px">We work regularly with leading advertising, media agencies and clients on various types of TV commercials.</p>

<div class="service-tag" style="left:700px;top:1910px">Film</div>
<div class="service-line" style="left:700px;top:1940px;height:20px"></div>
<div class="service-mark" style="left:700px;top:1960px" role="img" aria-label="Mascot holding a film reel icon"></div>
<p class="service-text" style="left:700px;top:2100px">Besides the fun stuff we do on TV series and commercials, we love to tinker around and produce our very own short films!</p>

<div class="service-tag" style="left:973px;top:1910px">Game</div>
<div class="service-line" style="left:973px;top:1940px;height:40px"></div>
<div class="service-mark" style="left:973px;top:1980px" role="img" aria-label="Mascot holding a game controller icon"></div>
<p class="service-text" style="left:973px;top:2120px">Our interactive arm offers the latest in games technology to bring our content and experience to another level!</p>

<div class="service-mark" style="left:217px;top:2270px" role="img" aria-label="Mascot holding a picture icon"></div>
<div class="service-line" style="left:217px;top:2390px;height:50px"></div>
<div class="service-tag" style="left:217px;top:2440px">AR/VR</div>
<p class="service-text" style="left:217px;top:2480px">Not just a new fad on the interactive landscape, we believe augmented reality and virtual reality are here to stay.</p>

<div class="service-mark" style="left:413px;top:2300px" role="img" aria-label="Mascot holding a calendar icon"></div>
<div class="service-line" style="left:413px;top:2420px;height:60px"></div>
<div class="service-tag" style="left:413px;top:2480px">Motion Capture</div>
<p class="service-text" style="left:413px;top:2520px">Armed with a mobile and wireless motion capture solution, we can do capture any kind of motion anywhere.</p>

<div class="service-mark" style="left:700px;top:2230px" role="img" aria-label="Mascot holding a camera icon"></div>
<div class="service-line" style="left:700px;top:2350px;height:55px"></div>
<div class="service-tag" style="left:700px;top:2405px">Co-productions</div>
<p class="service-text" style="left:700px;top:2445px">We partner with studios around the world to co-produce shows and share our characters with new audiences.</p>

<section class="partners"></section>
<h2 class="section-title on-dark" style="top:2790px">Our Partners</h2>
<div class="partner-row">
  <span class="partner">Harbourline</span>
  <span class="partner">Pebblecart</span>
  <span class="partner">TALLGRASS</span>
  <span class="partner">Quillmark</span>
  <span class="partner">BRIGHTVAULT</span>
</div>
<div class="dots" style="top:3090px"><span></span><span></span></div>

<h2 class="section-title" style="top:3245px">What's New?</h2>

<article class="news" style="left:122px;top:3375px">
  <h3>Signing Northwind Group as distributor for Milo</h3>
  <div class="meta">April 11, 2016 <i></i></div>
  <p>Talver Works creates original 3D animation content for TV that is both educational and entertaining. Talver Works creates original...</p>
  <span class="more">READ MORE &gt;&gt;</span>
</article>
<article class="news" style="left:480px;top:3375px">
  <h3>Possible AR/VR press coverage for Milo at Youth Festival, ATX</h3>
  <div class="meta">April 11, 2016 <i></i></div>
  <p>Talver Works creates original 3D animation content for TV that is both educational and entertaining. Talver Works creates original...</p>
  <span class="more">READ MORE &gt;&gt;</span>
</article>
<article class="news" style="left:822px;top:3375px">
  <h3>Moving of new office</h3>
  <div class="meta">April 11, 2016 <i></i></div>
  <p>Talver Works creates original 3D animation content for TV that is both educational and entertaining. Talver Works creates original...</p>
  <span class="more">READ MORE &gt;&gt;</span>
</article>
<article class="news" style="left:122px;top:3605px">
  <h3>Signing of Nora Season 2</h3>
  <div class="meta">April 11, 2016 <i></i></div>
  <p>Talver Works creates original 3D animation content for TV that is both educational and entertaining. Talver Works creates original...</p>
  <span class="more">READ MORE &gt;&gt;</span>
</article>
<article class="news" style="left:480px;top:3605px">
  <h3>Previous awards / festival selections for our short films</h3>
  <div class="meta">April 11, 2016 <i></i></div>
  <p>Talver Works creates original 3D animation content for TV that is both educational and entertaining. Talver Works creates original...</p>
  <span class="more">READ MORE &gt;&gt;</span>
</article>
<article class="news" style="left:822px;top:3605px">
  <h3>Previous news on release of Milo and Nora apps</h3>
  <div class="meta">April 11, 2016 <i></i></div>
  <p>Talver Works creates original 3D animation content for TV that is both educational and entertaining. Talver Works creates original...</p>
  <span class="more">READ MORE &gt;&gt;</span>
</article>

<section class="careers"></section>
<h2 class="section-title on-dark" style="top:3910px">Careers</h2>
<p class="careers-intro">We're a team of professionals. We have the animator, the director, the producer, the writer, the artist, the technologist, the gamer, the coder, the busy one, the office mama. Keeping everyone on deck is a shared belief in respect for teamwork, open communication and collaboration, with a love for action and an endless love for 3D.<strong>Currently, we're on the hunt for:</strong></p>

<div class="job" style="left:130px">
  <div class="job-brand"><i></i>TALVER WORKS</div>
  <div class="job-body">
    <h4>Assistant Director</h4>
    <div class="tags">3 days ago <b>Part time</b></div>
    <p>Proficiency with Maya, Blender and experience working in an animation production environment is required.</p>
  </div>
  <div class="job-foot"><span class="pay">$500 <small>/ month</small></span><span class="apply">APPLY NOW</span></div>
</div>
<div class="job" style="left:458px">
  <div class="job-brand"><i></i>TALVER WORKS</div>
  <div class="job-body">
    <h4>Animator</h4>
    <div class="tags">3 days ago <b>Full time</b></div>
    <p>Proficiency with Maya, Blender and experience working in an animation production environment is required.</p>
  </div>
  <div class="job-foot"><span class="pay">$3000 <small>/ month</small></span><span class="apply">APPLY NOW</span></div>
</div>
<div class="job" style="left:786px">
  <div class="job-brand"><i></i>TALVER WORKS</div>
  <div class="job-body">
    <h4>Modeler</h4>
    <div class="tags">3 days ago <b class="green">Contract</b></div>
    <p>Proficiency with Maya, Blender and experience working in an animation production environment is required.</p>
  </div>
  <div class="job-foot"><span class="pay">$900 <small>/ month</small></span><span class="apply">APPLY NOW</span></div>
</div>
<div class="dots grey" style="top:4474px"><span></span><span></span></div>

<section class="contact"></section>
<h2 class="section-title on-dark" style="top:4620px">Contact Us</h2>
<div class="contact-card">
  <p class="lead">Contact us at the following for projects, co-production and general enquiries: hello@talver-works.example</p>
  <div class="loc-title">Our locations</div>
  <p class="office" style="left:40px"><b>Singapore (Main Office)</b>Talver Works Pte Ltd<br>1000 Harbour Road<br>#03-08 Lantern Building<br>Singapore 310000</p>
  <p class="office" style="left:260px;top:130px"><b>Bangalore</b>Talver Works Studios Pvt Ltd<br>12th Floor, Level 5<br>Orchard Block<br>Riverside Tech Park<br>Bangalore 560000</p>
  <div class="map" role="img" aria-label="Map showing the Singapore office location"></div>
</div>

<footer class="site-footer">
  <p>Copyright © 2016 - Talver Works. All Rights Reserved.</p>
  <span class="to-top"></span>
</footer>

</body>
</html>
```